Website for Painting Company

Hi,
We are after a Wordpress website design with CSS/HTML Theme for our painting company based in Brisbane, Australia. Our business name is Felix Morrow Painting Contractors and we have been trading for 33 years.
We want a website that is modern and fresh with a professional image. Our organisation does Commercial, Residential and Insurance Painting projects. I have listed a couple of similar websites that we like the look and feel of. These are a guide only and we are happy to see you own designs with a similar professional image.
http://www.kelbrookcoatings.com.au/
http://www.tidewellfinishes.com.au/
We are a member of Guild Decorators Australia and I have supplied the logo named "gda" which I have included in the files I have uploaded.
We want a five page site. These are Home Page, Residential, Commercial, Insurance and Contact Us.
I have also uploaded our logo and some pictures labeled Logo,Residential, Commercial, Insurance and Homepage. These should be used on each page listed above.
Updates
Project Deadline Extended
Reason: We are extending because we need more time to go through the designs and give feedback. There are many fantastic designs. Thank you everyone who has contributed!!!!
All the best
Derek
Industry/Entity Type
Painting
Requirements
Must have
- We want a five page site. These are Home Page, Residential, Commercial, Insurance and Contact Us.

```html
<!DOCTYPE html>
<html lang="en">
<head>
<meta charset="utf-8">
<title>Felix Morrow Painting Contractors</title>
<link rel="stylesheet" href="https://fonts.googleapis.com/css2?family=Arimo:wght@400;700&family=Quicksand:wght@500&display=swap">
<style>
  :root {
    --red: #e0232a;
    --red-soft: #ee5a52;
    --ink: #1f1f1f;
    --body: #2b2b2b;
    --muted: #555;
    --page: #f1f1f1;
    --panel: #f3f3f3;
    --rule: #cfcfcf;
    --frame: #6a6a6a;
    --footer: #3b3b3b;
    --footer-text: #ffffff;
  }
  * { box-sizing: border-box; margin: 0; padding: 0; }
  html, body { width: 1022px; height: 1200px; overflow: hidden; }
  body {
    position: relative;
    background: linear-gradient(180deg, #ececec 0%, #f4f4f4 40%, #f1f1f1 100%);
    font-family: "Arimo", Arial, sans-serif;
    color: var(--body);
  }
  .topbar { position: absolute; left: 0; top: 0; width: 1022px; height: 9px; background: var(--footer); }

  .brand { position: absolute; left: 74px; top: 40px; display: flex; align-items: flex-start; gap: 8px; }
  .brand-mark { width: 16px; height: 16px; background: var(--red); margin-top: 4px; }
  .brand-name { font-weight: 700; font-size: 20px; line-height: 25px; color: var(--red); }

  .quote { position: absolute; left: 740px; top: 15px; width: 196px; text-align: right; }
  .quote-label { font-size: 16px; color: var(--ink); padding-right: 10px; }
  .quote-phone {
    margin-top: 3px; display: inline-flex; align-items: center; gap: 8px;
    background: var(--red-soft); color: #fff; font-size: 22px; letter-spacing: .5px;
    padding: 4px 12px; border-radius: 4px;
  }

  .nav {
    position: absolute; left: 408px; top: 112px; width: 520px; height: 28px;
    border-bottom: 1px solid var(--rule);
    display: flex; justify-content: space-between; align-items: flex-start;
  }
  .nav a {
    font-weight: 700; font-size: 13px; line-height: 16px; white-space: nowrap;
    text-decoration: none; color: var(--red);
  }
  .nav a.current { color: var(--ink); font-weight: 400; }
  .nav .sep { width: 1px; height: 20px; background: #bbb; margin-top: -2px; }

  .slider {
    position: absolute; left: 65px; top: 156px; width: 880px; height: 380px;
    border: 3px solid var(--frame); box-shadow: 0 6px 8px rgba(0,0,0,.18);
  }
  .slider-photo { width: 100%; height: 100%; background: linear-gradient(160deg, #e9e6e2 0%, #d9cfc4 35%, #bfae9b 60%, #ece9e4 85%); }
  .slider-dots { position: absolute; right: 20px; bottom: 10px; display: flex; gap: 8px; }
  .slider-dots span { width: 10px; height: 10px; border-radius: 50%; background: #333; }
  .slider-dots span:first-child { background: var(--red); }

  .divider { position: absolute; left: 0; top: 547px; width: 1022px; height: 1px; background: #d6d6d6; }

  .project { position: absolute; top: 555px; width: 266px; height: 293px; border: 1px solid var(--rule); background: var(--panel); }
  .project h2 {
    margin: 12px 12px 0; padding-bottom: 4px; border-bottom: 1px solid var(--rule);
    font-family: "Quicksand", sans-serif; font-weight: 500; font-size: 19px; color: var(--red); letter-spacing: .6px;
    white-space: nowrap;
  }
  .project h2 .num { color: var(--ink); font-family: "Arimo", Arial, sans-serif; font-size: 17px; letter-spacing: 0; }
  .project-photo { margin: 14px 7px 0; height: 112px; border: 2px solid #999; box-shadow: 0 3px 5px rgba(0,0,0,.25); }
  .project p { margin: 18px 7px 0; font-size: 12px; line-height: 17px; text-align: justify; }
  .more {
    position: absolute; left: 203px; top: 256px; width: 40px; height: 25px; border-radius: 4px;
    background: var(--red-soft); color: #fff; font-weight: 700; font-size: 12px; text-align: center; line-height: 25px;
  }
  .p1 { left: 67px; } .p2 { left: 368px; } .p3 { left: 666px; }

  .section-title { font-family: "Quicksand", sans-serif; font-weight: 500; font-size: 19px; color: var(--red); letter-spacing: 1px; position: absolute; }

  .latest-title { left: 77px; top: 867px; }
  .latest-photo { position: absolute; left: 74px; top: 907px; width: 216px; height: 116px; border: 3px solid #555; background: linear-gradient(150deg, #f2f2f0, #c9b79f 55%, #7a6452); }
  .latest-caption { position: absolute; left: 73px; top: 1039px; width: 290px; font-size: 12.5px; line-height: 16.5px; color: var(--muted); }
  .latest-caption strong { display: block; color: var(--ink); font-size: 13px; margin-bottom: 1px; }

  .vrule { position: absolute; width: 1px; background: var(--rule); top: 880px; height: 203px; }
  .vr1 { left: 367px; } .vr2 { left: 642px; }

  .about-title { left: 390px; top: 873px; }
  .about-text { position: absolute; left: 387px; top: 907px; width: 230px; font-size: 12px; line-height: 16.8px; text-align: justify; }
  .member { position: absolute; left: 387px; top: 979px; font-size: 12px; }
  .member-badge { position: absolute; left: 388px; top: 1001px; width: 84px; height: 77px; border: 1px solid #2a4fbf; background: #fff; }
  .member-badge span { position: absolute; left: 22px; top: 18px; width: 38px; height: 38px; border-radius: 50%; background: #2a4fbf; }

  .colour-promo {
    position: absolute; left: 672px; top: 898px; width: 261px; height: 154px; border-radius: 8px;
    background: linear-gradient(120deg, #e34848 0%, #e34848 30%, #ddd8cc 31%, #e5df9a 60%, #a8d43c 100%);
    box-shadow: 0 2px 4px rgba(0,0,0,.2);
  }

  .footer { position: absolute; left: 0; top: 1121px; width: 1022px; height: 79px; background: var(--footer); color: var(--footer-text); }
  .footer-nav { position: absolute; left: 70px; top: 29px; font-size: 13px; }
  .footer-nav a { color: var(--footer-text); text-decoration: none; }
  .footer-nav .sep { margin: 0 7px; }
  .copyright { position: absolute; right: 64px; top: 53px; font-size: 11px; letter-spacing: .3px; }
</style>
</head>
<body>
  <div class="topbar"></div>

  <div class="brand">
    <div class="brand-mark"></div>
    <div class="brand-name">Felix Morrow<br>Painting Contractors</div>
  </div>

  <div class="quote">
    <div class="quote-label">Get a free quote</div>
    <div class="quote-phone">
      <svg width="16" height="16" viewBox="0 0 24 24" aria-hidden="true"><path fill="#fff" d="M6.6 10.8a15.1 15.1 0 0 0 6.6 6.6l2.2-2.2c.3-.3.7-.4 1-.2 1.1.4 2.3.6 3.6.6.6 0 1 .4 1 1V20c0 .6-.4 1-1 1A17 17 0 0 1 3 4c0-.6.4-1 1-1h3.5c.6 0 1 .4 1 1 0 1.3.2 2.5.6 3.6.1.3 0 .7-.2 1z"/></svg>
      123 004 5512
    </div>
  </div>

  <nav class="nav">
    <a href="#" class="current">HOME</a><span class="sep"></span>
    <a href="#">RESIDENTIAL</a><span class="sep"></span>
    <a href="#">COMMERCIAL</a><span class="sep"></span>
    <a href="#">INSURANCE</a><span class="sep"></span>
    <a href="#">CONTACT US</a>
  </nav>

  <div class="slider">
    <div class="slider-photo" role="img" aria-label="Bright open-plan living and dining room with white floors and cream furniture"></div>
    <div class="slider-dots"><span></span><span></span><span></span><span></span></div>
  </div>

  <div class="divider"></div>

  <section class="project p1">
    <h2><span class="num">01.</span> Residential Projects</h2>
    <div class="project-photo" role="img" aria-label="Warm yellow painted living room with fireplace" style="background:linear-gradient(135deg,#f2d27a,#d89a48 55%,#8a5a34);"></div>
    <p>Lorem ipsum dolor sit amet, quas abhorreant mel cu, sea an veri qualisque mediocritatem. Cu mei autem neglegentur, at quodsi omit­tam per.</p>
    <div class="more">more</div>
  </section>

  <section class="project p2">
    <h2><span class="num">02.</span> Commercial Projects</h2>
    <div class="project-photo" role="img" aria-label="Modern interior with open timber staircase" style="background:linear-gradient(150deg,#f3f3f1,#c8b8a0 55%,#6e5845);"></div>
    <p>Lorem ipsum dolor sit amet, quas abhorreant mel cu, sea an veri qualisque mediocritatem. Cu mei autem neglegentur, at quodsi omit­tam per.</p>
    <div class="more">more</div>
  </section>

  <section class="project p3">
    <h2><span class="num">03.</span> Insurance Projects</h2>
    <div class="project-photo" role="img" aria-label="White rendered house under a blue sky" style="background:linear-gradient(180deg,#3f78c8 0%,#8fb6e6 45%,#e9ecef 60%,#9aa08a 100%);"></div>
    <p>Lorem ipsum dolor sit amet, quas abhorreant mel cu, sea an veri qualisque mediocritatem. Cu mei autem neglegentur, at quodsi omit­tam per.</p>
    <div class="more">more</div>
  </section>

  <h2 class="section-title latest-title">Latest Projects</h2>
  <div class="latest-photo" role="img" aria-label="Recent project: interior with timber staircase"></div>
  <div class="latest-caption">
    <strong>Lumoleie lacene anrit ma hasellus porta.</strong>
    Senasc ridiculus mue feugiat malesuada ntasen aserc seuis ultricies pharcn maleda.
  </div>

  <div class="vrule vr1"></div>

  <h2 class="section-title about-title">About us</h2>
  <p class="about-text">Lorem ipsum dolor sit amet, sea libris graeci deserunt ad, et scripserit interpre­taris nam. Mei ne nullam animal. Vix quod graecis instructior et.</p>
  <p class="member">We are member of</p>
  <div class="member-badge" role="img" aria-label="Guild Decorators Australia membership badge"><span></span></div>

  <div class="vrule vr2"></div>

  <div class="colour-promo" role="img" aria-label="Find your colour promotion: hand holding a fan of paint colour swatches, ask our colour expert"></div>

  <footer class="footer">
    <div class="footer-nav">
      <a href="#">Home</a><span class="sep">|</span><a href="#">Residential</a><span class="sep">|</span><a href="#">Commercial</a><span class="sep">|</span><a href="#">Insurance</a><span class="sep">|</span><a href="#">Contact Us</a>
    </div>
    <div class="copyright">Copyright 2012 Felix Morrow and Co. All rights reserved</div>
  </footer>
</body>
</html>
```